Refer a Friend A5 Flyer for Healthcare Staff

We need an A5 flyer that we can hand out to existing and new staff members promoting our Refer a friend Scheme. We need the leaflet to encourage staff to talk to their family and friends about joining our Healthcare Agency, which provides staff to local care related establishments. Using our logo and brand colours blue and green, as per our website, the final design will need to clearly convey the benefits and attractions of referring additional staff to the team. In addition is the promotion of our SocialHub page, requesting staff to like the page and to like and share various posts.

Target Market(s)

Healthcare and potential Healthcare Staff

Industry/Entity Type

Healthcare

Colors
33b8a4
3277b5

Requirements
Must have
• Company Logo, Brand colours,
• text; "Refer a Friend and receive a £50 Bonus after just 1 completed shift"
• text; "3 easy steps to refer a friend, 1 Fill out your name on the back of your Business Card 2 Hand the card to your friend or any person you wish to refer, 3 ask your friend to present the card to us when they attend their interview"
• text; "Like and share any of our Open Days on SocialHub for a chance to win a prize, you can find us easily by searching @CarewellPlacementGroup"
• text; "Like our Page to stay up to date with our events and offers"
Nice to have
• care worker / elderly care / support worker pictures
• Content / pics from website www.carewellplacementgroup.co.uk

```html
<!DOCTYPE html>
<html lang="en">
<head>
<meta charset="utf-8">
<title>Refer a Friend Flyer</title>
<link rel="stylesheet" href="https://fonts.googleapis.com/css2?family=Arimo:wght@700&family=Lato:wght@400;700&display=swap">
<style>
  :root {
    --stage: #4a4a4a;
    --brand-blue: #3277b5;
    --sky-blue: #4a8cc4;
    --brand-teal: #33b8a4;
    --teal-light: #3cc2ae;
    --ink: #1c1c1c;
    --paper: #ffffff;
  }
  html, body {
    margin: 0;
    width: 1200px;
    height: 1200px;
    overflow: hidden;
    background: var(--stage);
  }
  .flyer {
    position: absolute;
    left: 218px;
    top: 73px;
    width: 772px;
    height: 1083px;
    overflow: hidden;
    background: linear-gradient(180deg, var(--sky-blue) 0%, #46a6bf 45%, var(--teal-light) 100%);
    font-family: "Lato", sans-serif;
    color: var(--paper);
  }
  .logo-disc {
    position: absolute;
    left: 382px;
    top: -401px;
    width: 688px;
    height: 688px;
    border-radius: 50%;
    background: var(--paper);
  }
  .brand {
    position: absolute;
    left: 440px;
    top: 50px;
    width: 300px;
    display: flex;
    align-items: center;
    gap: 12px;
  }
  .brand-dot {
    width: 22px;
    height: 22px;
    border-radius: 50%;
    background: var(--brand-teal);
    flex: none;
  }
  .brand-name {
    font-family: "Lato", sans-serif;
    font-weight: 400;
    font-size: 34px;
    line-height: 1.05;
    color: var(--brand-blue);
  }
  .photo {
    position: absolute;
    left: 470px;
    top: 216px;
    width: 302px;
    height: 867px;
    border-radius: 150px 150px 0 0;
    background: linear-gradient(180deg, #d9c9a8 0%, #f2f2f2 30%, #2e6f8a 60%, #eef1f3 100%);
  }
  .headline {
    position: absolute;
    left: 28px;
    top: 36px;
    margin: 0;
    font-family: "Arimo", sans-serif;
    font-weight: 700;
    line-height: 1;
  }
  .headline .big { display: block; font-size: 88px; letter-spacing: 1px; }
  .headline .mid { display: block; font-size: 67px; margin-top: 10px; }
  .offer {
    position: absolute;
    left: 28px;
    top: 198px;
    margin: 0;
    font-family: "Arimo", sans-serif;
    font-weight: 700;
    font-size: 44px;
    line-height: 51px;
  }
  .divider {
    position: absolute;
    left: 0;
    top: 364px;
    width: 560px;
    border-top: 3px dotted rgba(255,255,255,0.85);
  }
  .steps-title {
    position: absolute;
    left: 33px;
    top: 378px;
    margin: 0;
    font-family: "Arimo", sans-serif;
    font-weight: 700;
    font-size: 43px;
    line-height: 43px;
  }
  .steps-rule {
    position: absolute;
    left: 0;
    top: 474px;
    width: 306px;
    height: 5px;
    background: var(--paper);
    clip-path: polygon(0 0, 100% 0, 98% 100%, 0 100%);
  }
  .step {
    position: absolute;
    left: 29px;
    display: flex;
    gap: 14px;
  }
  .step-num {
    width: 64px;
    height: 64px;
    background: var(--paper);
    color: var(--brand-blue);
    font-family: "Arimo", sans-serif;
    font-weight: 700;
    font-size: 38px;
    display: flex;
    align-items: center;
    justify-content: center;
    flex: none;
  }
  .step-text {
    margin: -4px 0 0;
    font-weight: 400;
    font-size: 24px;
    line-height: 32px;
    white-space: nowrap;
  }
  .info-panel {
    position: absolute;
    left: 0;
    top: 813px;
    width: 470px;
    height: 270px;
    background: var(--paper);
    color: var(--ink);
  }
  .info-panel p { margin: 0; }
  .social {
    position: absolute;
    left: 33px;
    font-size: 19px;
    line-height: 21px;
  }
  .cta {
    position: absolute;
    left: 30px;
    top: 146px;
    font-weight: 700;
    font-size: 25px;
    line-height: 26px;
    color: var(--brand-blue);
  }
  .cta-rule {
    position: absolute;
    left: 0;
    top: 203px;
    width: 272px;
    height: 5px;
    background: var(--brand-teal);
    clip-path: polygon(0 0, 100% 0, 97% 100%, 0 100%);
  }
  .web {
    position: absolute;
    left: 30px;
    top: 216px;
    font-weight: 700;
    font-size: 18px;
  }
</style>
</head>
<body>
  <main class="flyer">
    <div class="logo-disc"></div>
    <div class="brand">
      <span class="brand-dot"></span>
      <span class="brand-name">Carewell<br>Placement</span>
    </div>

    <div class="photo" role="img" aria-label="Smiling female doctor in white coat and teal scrubs with a stethoscope"></div>

    <h1 class="headline"><span class="big">REFER</span><span class="mid">A FRIEND</span></h1>
    <p class="offer">and receive a<br>£50 Bonus after just<br>1 completed shift</p>

    <div class="divider"></div>

    <h2 class="steps-title">3 EASY STEPS to<br>refer a friend</h2>
    <div class="steps-rule"></div>

    <div class="step" style="top:493px">
      <span class="step-num">1.</span>
      <p class="step-text">Fill out your name on the<br>back of your Business Card</p>
    </div>
    <div class="step" style="top:603px">
      <span class="step-num">2.</span>
      <p class="step-text">Hand the card to your friend or<br>any person you wish to refer</p>
    </div>
    <div class="step" style="top:708px">
      <span class="step-num">3.</span>
      <p class="step-text">Ask your friend to present the<br>card to us when they attend<br>their interview</p>
    </div>

    <section class="info-panel">
      <p class="social" style="top:12px">Like and share any of our Open Days on SocialHub<br>for a chance to win a prize, you can find us easily<br>by searching @CarewellPlacementGroup</p>
      <p class="social" style="top:90px">Like our Page to stay up to date with our<br>events and offers</p>
      <p class="cta">Visit our website for more<br>details &amp;information</p>
      <div class="cta-rule"></div>
      <p class="web">www.carewellplacementgroup.co.uk</p>
    </section>
  </main>
</body>
</html>
```